Brook Forge - Crypto Currency Miner Powered by Renewable Energy Website

We Need Web Pages Design for Website for Crypto Currency Miner

Serivices include:
Mining Rig Sales
Housing for Rigs turnkey on renewable energy grid
Cloud Mining term packages
Updates

http://www.vaultrigratings.example (Competitors sites)

Target Market(s)

Investers for Mining Rigs and terms for 1,2 or 3 years of Hash rate

Industry/Entity Type

Mining

Number of Pages Required

5+ page

Font styles to use
Sans Serif

Colors
add136
9bcb3c
606060
474747
ffc214
cadf82
fbee3e
876aae
6b449b

Requirements
Must have
• Pictures of Solar, Wind and power Factor Correction units
Nice to have
• e-commerce platform so contract terms can be purchased through website
Should not have
• Heavy construction equipment

```html
<!DOCTYPE html>
<html lang="en">
<head>
<meta charset="utf-8">
<title>Brook Forge – Renewable Crypto Mining</title>
<link href="https://fonts.googleapis.com/css2?family=Roboto:ital,wght@0,400;0,500;0,700;1,400&display=swap" rel="stylesheet">
<style>
:root{
  --green:#2ba33a;
  --green-light:#9bcb3c;
  --green-pale:#eef5dc;
  --bg-soft:#f2f6e6;
  --yellow:#ffc214;
  --red:#e0262b;
  --text:#474747;
  --muted:#606060;
  --dark:#2b2b2b;
  --white:#fff;
}
*{box-sizing:border-box;margin:0;padding:0}
html,body{width:1200px;height:3163px;overflow:hidden}
body{font-family:"Roboto",Arial,sans-serif;color:var(--text);background:var(--white);position:relative}
.abs{position:absolute}
.wrap{position:absolute;left:243px;width:712px}

/* header */
.topbar{top:0;left:0;width:1200px;height:59px;background:linear-gradient(90deg,#1e9a3a,var(--green) 50%,#39ad3d)}
.navbar{top:59px;left:0;width:1200px;height:30px;background:var(--green-pale)}
.logo{top:0;left:243px;width:120px;height:89px;background:var(--white);display:flex;flex-direction:column;align-items:center;justify-content:center;z-index:3;box-shadow:0 2px 6px rgba(0,0,0,.12)}
.logo .dot{width:30px;height:30px;border-radius:50%;background:var(--green);margin-bottom:6px}
.logo span{font-weight:700;font-size:16px;color:var(--green)}
.contact{top:12px;display:flex;align-items:center;gap:8px;color:var(--white);font-size:11px;line-height:1.3}
.contact b{display:block;font-size:11px}
.contact .ic{width:26px;height:26px;border-radius:50%;background:var(--yellow);display:flex;align-items:center;justify-content:center}
.menu{top:59px;left:422px;display:flex;height:30px;align-items:center;font-size:11px;color:var(--text)}
.menu a{padding:0 10px;line-height:30px;text-decoration:none;color:inherit}
.menu a.on{background:var(--yellow)}
.search{top:64px;left:833px;width:122px;height:20px;border-radius:10px;background:var(--white);font-size:9px;color:#999;display:flex;align-items:center;padding-left:22px}
.search svg{position:absolute;left:8px;top:5px}

/* hero */
.hero{top:89px;left:0;width:1200px;height:438px;background:linear-gradient(180deg,#6d93c4 0%,#b7cde2 35%,#8aa0a8 55%,#3f6a2f 80%,#4b8a2a 100%)}
.hero h1{position:absolute;top:112px;width:100%;text-align:center;font-size:36px;font-weight:700;color:#111}
.hero p{position:absolute;top:170px;left:372px;width:456px;text-align:center;font-size:11px;line-height:15px;color:#222}
.btn{display:inline-block;font-size:10px;font-weight:700;text-transform:uppercase;padding:0 14px;line-height:32px;border-radius:3px}
.btn-red{background:var(--red);color:var(--white)}
.btn-yellow{background:var(--yellow);color:#222}
.hero .btns{position:absolute;top:248px;left:0;width:100%;display:flex;justify-content:center;gap:10px}
.dots{position:absolute;top:408px;left:0;width:100%;display:flex;justify-content:center;gap:5px}
.dots i{width:10px;height:6px;background:var(--white);border-radius:3px;transform:skewX(-25deg)}
.dots i:first-child{background:var(--green-light)}

/* services */
.services{top:527px;left:0;width:1200px;height:458px;background:linear-gradient(90deg,#f1f4e8,#e7eed7)}
.section-title{position:absolute;width:100%;text-align:center;font-size:28px;font-weight:500;color:#1c1c1c}
.service{position:absolute;top:112px;width:230px;text-align:center}
.ring{width:160px;height:160px;border-radius:50%;margin:0 auto;border:6px solid var(--green);display:flex;align-items:center;justify-content:center;background:var(--white)}
.ring div{width:128px;height:128px;border-radius:50%;background:radial-gradient(circle at 50% 40%,#4dbf3f,#1f9134);display:flex;align-items:center;justify-content:center}
.service h3{margin-top:28px;font-size:13px;font-weight:500;color:#222;line-height:17px}
.service p{margin-top:10px;font-size:10.5px;line-height:15px;color:#777;padding:0 20px}

/* welcome */
.welcome{top:985px;left:0;width:1200px;height:386px;background:linear-gradient(90deg,#5f86a6 0%,#8ea8b8 40%,#e9cfa6 75%,#f5b98c 100%)}
.welcome-card{top:48px;left:243px;width:347px;height:285px;background:var(--yellow);border-radius:16px;padding:20px 26px;color:#222}
.welcome-card .small{font-size:13px;margin-left:44px}
.welcome-card h2{font-size:26px;font-weight:700;margin-left:44px;line-height:28px}
.welcome-card .badge{position:absolute;left:26px;top:24px;width:36px;height:36px;border-radius:50%;background:#1b1b1b}
.welcome-card p{margin-top:8px;font-size:10.5px;line-height:15px}
.welcome-card .btn{margin-top:20px}

/* products */
.products{top:1371px;left:0;width:1200px;height:460px;background:var(--bg-soft)}
.card{position:absolute;top:109px;width:225px;height:302px;background:var(--white);text-align:center}
.card .ph{height:160px}
.card h4{margin:18px 18px 0;font-size:11.5px;font-weight:700;line-height:15px;color:#222}
.card .price{margin-top:8px;font-size:18px;font-weight:700;color:var(--red)}
.card .btn{margin-top:10px;line-height:26px;font-size:9px;padding:0 12px}

/* testimonials */
.testi-band{top:1831px;left:0;width:1200px;height:320px;background:linear-gradient(90deg,#1f9a3a,#39a83a 50%,#7bbd3f)}
.testi-band h2{position:absolute;top:112px;left:243px;font-size:28px;font-weight:500;line-height:32px;color:var(--white)}
.testi{top:2151px;left:0;width:1200px;height:201px;background:var(--white)}
.quote{position:absolute;top:-36px;width:236px;text-align:center}
.avatar{width:74px;height:74px;border-radius:50%;border:5px solid var(--green-light);margin:0 auto;background:#cfd8c4}
.qmark{width:22px;height:22px;border-radius:50%;background:var(--yellow);margin:-12px auto 0;position:relative;font-size:16px;font-weight:700;line-height:26px;color:#333}
.quote p{margin-top:8px;font-size:10.5px;line-height:15px;font-style:italic;color:#666}
.quote .name{margin-top:12px;font-size:13px;font-weight:500;color:var(--red)}
.arrow{position:absolute;top:76px;width:16px;height:16px;border-radius:50%;border:1px solid #999;font-size:10px;line-height:14px;text-align:center;color:#777}

/* blog & why */
.blog{top:2352px;left:0;width:1200px;height:453px;background:var(--bg-soft)}
.blog h2{position:absolute;top:50px;left:243px;font-size:21px;font-weight:500;color:#1c1c1c}
.blog .rule{position:absolute;top:84px;left:243px;width:150px;height:2px;background:var(--green-light)}
.post{position:absolute;top:109px;width:200px}
.post .ph{height:165px}
.post h4{margin-top:22px;font-size:11.5px;font-weight:700;line-height:15px;color:#222}
.post p{margin-top:8px;font-size:10.5px;line-height:15px;color:#666}
.post a{display:block;margin-top:6px;font-size:10px;color:var(--red);text-decoration:none}
.why{position:absolute;top:54px;left:671px;width:284px;height:346px;background:var(--yellow);border-radius:14px;padding:22px 24px;color:#222}
.why h3{font-size:21px;font-weight:500;margin-bottom:16px}
.why-item{display:flex;gap:12px;margin-bottom:18px}
.why-item .ic{flex:0 0 34px;height:34px;border-radius:50%;border:2px solid #222;display:flex;align-items:center;justify-content:center}
.why-item h5{font-size:13px;font-weight:700}
.why-item p{font-size:10px;line-height:14px;margin-top:4px}

/* footer */
.footer{top:2805px;left:0;width:1200px;height:358px;background:var(--dark);color:#cfcfcf}
.news{position:absolute;top:22px;left:243px;display:flex;align-items:center;gap:14px}
.news .title{font-size:12px;font-weight:700;color:var(--white);line-height:13px;padding-left:46px;position:relative}
.news .title svg{position:absolute;left:0;top:2px}
.news .field{width:202px;height:28px;background:var(--white);font-size:9px;color:#999;padding:9px 8px}
.news .btn{line-height:28px;font-size:10px}
.social{position:absolute;top:24px;left:803px;display:flex;gap:8px}
.social i{width:24px;height:24px;border-radius:50%;background:#8a8a8a;display:block}
.fdiv{position:absolute;top:16px;left:762px;width:1px;height:190px;background:#444}
.fcol{position:absolute;top:88px;font-size:10px;line-height:16px}
.fcol h6{font-size:11.5px;font-weight:700;color:var(--white);margin-bottom:8px}
.pay{position:absolute;top:268px;left:0;width:100%;display:flex;justify-content:center;gap:8px}
.pay i{width:42px;height:24px;border-radius:3px;background:#d9d9d9;display:block}
.copy{position:absolute;top:305px;width:100%;text-align:center;font-size:10px;color:#aaa}
</style>
</head>
<body>

<header>
  <div class="abs topbar"></div>
  <div class="abs navbar"></div>
  <div class="abs logo"><div class="dot"></div><span>Brook Forge</span></div>

  <div class="abs contact" style="left:586px">
    <div class="ic"><svg width="12" height="12" viewBox="0 0 24 24"><path d="M6.6 10.8a15 15 0 0 0 6.6 6.6l2.2-2.2c.3-.3.7-.4 1-.2 1.1.4 2.3.6 3.6.6.6 0 1 .4 1 1V20c0 .6-.4 1-1 1A17 17 0 0 1 3 4c0-.6.4-1 1-1h3.5c.6 0 1 .4 1 1 0 1.3.2 2.5.6 3.6.1.3 0 .7-.2 1z" fill="#222"/></svg></div>
    <div><b>555-014-2270</b>Toll-Free Today!</div>
  </div>
  <div class="abs contact" style="left:710px">
    <div class="ic"><svg width="12" height="12" viewBox="0 0 24 24"><circle cx="12" cy="8" r="4" fill="#222"/><path d="M4 21c0-4.4 3.6-7 8-7s8 2.6 8 7z" fill="#222"/></svg></div>
    <div><b>My Account</b>Create New Account</div>
  </div>
  <div class="abs contact" style="left:852px">
    <div class="ic"><svg width="12" height="12" viewBox="0 0 24 24"><path d="M5 8h14l-1.5 12h-11z" fill="#222"/><path d="M9 8a3 3 0 0 1 6 0" stroke="#222" stroke-width="2" fill="none"/></svg></div>
    <div><b>Shopping Cart</b>0 Items - $0.00</div>
  </div>

  <nav class="abs menu">
    <a class="on">Home</a><a>About</a><a>Services</a><a>Products</a><a>Testimonials</a><a>Blog</a><a>Contact</a>
  </nav>
  <div class="abs search"><svg width="10" height="10" viewBox="0 0 24 24"><circle cx="10" cy="10" r="7" stroke="#2ba33a" stroke-width="3" fill="none"/><path d="M15 15l6 6" stroke="#2ba33a" stroke-width="3"/></svg>Enter keywords</div>
</header>

<section class="abs hero" role="img" aria-label="Rows of solar panels under a bright cloudy sky with a grass path between them">
  <h1>Start The Brook Forge Today!</h1>
  <p>Sed non mauris vitae erat consequat auctor eu in elit. Class aptent taciti sociosqu ad litora torquent per conubia nostra, per inceptos himenaeos. Mauris in erat justo. Nullam ac urna eu felis dapibus condimentum sit amet a augue.</p>
  <div class="btns"><span class="btn btn-red">Get Started Today!</span><span class="btn btn-yellow">Contact Now Today!</span></div>
  <div class="dots"><i></i><i></i><i></i><i></i></div>
</section>

<section class="abs services">
  <h2 class="section-title" style="top:42px">Services We Provide</h2>

  <div class="service" style="left:243px">
    <div class="ring"><div><svg width="60" height="60" viewBox="0 0 60 60" fill="none" stroke="#fff" stroke-width="3"><rect x="16" y="16" width="28" height="28" rx="3"/><rect x="24" y="24" width="12" height="12"/><path d="M22 10v6M30 10v6M38 10v6M22 44v6M30 44v6M38 44v6M10 22h6M10 30h6M10 38h6M44 22h6M44 30h6M44 38h6"/></svg></div></div>
    <h3>Mining Rig Sales</h3>
    <p>Class aptent taciti sociosqu ad litora torquent per conubia nostra, per inceptos himenaeos. Mauris in erat justo.</p>
  </div>
  <div class="service" style="left:486px">
    <div class="ring"><div><svg width="60" height="60" viewBox="0 0 60 60" fill="none" stroke="#fff" stroke-width="3"><path d="M48 30a18 18 0 1 1-6-13.4"/><path d="M42 10v7h-7"/><path d="M32 18l-8 14h9l-6 12" stroke-linejoin="round"/></svg></div></div>
    <h3>Housing for Rigs Turnkey<br>on Renewable Energy Grid</h3>
    <p>Class aptent taciti sociosqu ad litora torquent per conubia nostra, per inceptos himenaeos. Mauris in erat justo.</p>
  </div>
  <div class="service" style="left:729px">
    <div class="ring"><div><svg width="64" height="60" viewBox="0 0 64 60" fill="none" stroke="#fff" stroke-width="3"><path d="M18 44h28a10 10 0 0 0 0-20 14 14 0 0 0-27-3A11 11 0 0 0 18 44z"/><path d="M30 36l12-12M38 24h4v4"/></svg></div></div>
    <h3>Cloud Mining Term<br>Packages</h3>
    <p>Class aptent taciti sociosqu ad litora torquent per conubia nostra, per inceptos himenaeos. Mauris in erat justo.</p>
  </div>
</section>

<section class="abs welcome" role="img" aria-label="Solar panel field with a wind turbine against a hazy sunset">
  <div class="abs welcome-card">
    <div class="badge"></div>
    <div class="small">Welcome to</div>
    <h2>The Brook Forge</h2>
    <p>Nam nec tellus a odio tincidunt auctor a ornare odio. Sed non mauris vitae erat consequat auctor eu in elit. Class aptent taciti sociosqu ad litora torquent per conubia nostra, per inceptos himenaeos. Mauris in erat justo. Nullam ac urna eu felis dapibus condimentum sit amet a augue. Sed non fermentum nunc. Etiam pharetra, erat sed fermentum velit feugiat, velit mauris egestas quam, ut aliquam massa nisl quis neque. Suspendisse in orci enim.</p>
    <span class="btn btn-red">Get Started Today!</span>
  </div>
</section>

<section class="abs products">
  <h2 class="section-title" style="top:48px">Featured Products</h2>
  <div class="card" style="left:243px">
    <div class="ph" role="img" aria-label="Wind turbines on a coastal hillside under blue sky" style="background:linear-gradient(180deg,#3f8fd6,#9cc9ec 60%,#7a7f6c)"></div>
    <h4>Awesome Lorem ipsum dolor sit amet dosis lipsum it</h4>
    <div class="price">$299.99</div>
    <span class="btn btn-yellow">Add to Cart</span>
  </div>
  <div class="card" style="left:487px">
    <div class="ph" role="img" aria-label="Solar panels in a green field at sunrise" style="background:linear-gradient(180deg,#3b7fd0,#f2d27a 45%,#3f6ea4 70%,#4c8d2b)"></div>
    <h4>Awesome Lorem ipsum dolor sit amet dosis lipsum it</h4>
    <div class="price">$199.99</div>
    <span class="btn btn-yellow">Add to Cart</span>
  </div>
  <div class="card" style="left:730px">
    <div class="ph" role="img" aria-label="Close view of a wind turbine against a blue sky" style="background:linear-gradient(160deg,#2e6fa8,#7fb0d6 60%,#d7e6f0)"></div>
    <h4>Awesome Lorem ipsum dolor sit amet dosis lipsum it</h4>
    <div class="price">$389.99</div>
    <span class="btn btn-yellow">Add to Cart</span>
  </div>
</section>

<section class="abs testi-band" role="img" aria-label="Family standing in front of solar panels, tinted green">
  <h2>What About<br>Our Customer Say</h2>
</section>
<section class="abs testi">
  <div class="arrow" style="left:219px">&#8249;</div>
  <div class="arrow" style="left:965px">&#8250;</div>
  <div class="quote" style="left:257px">
    <div class="avatar" role="img" aria-label="Customer portrait"></div>
    <div class="qmark">&ldquo;</div>
    <p>"Duis sed odio sit amet nibh vulputate as non mauris vitae erat consequat auctor eu in elit. Class aptent taciti sociosqu ad litora torquent per conubia nostra, per inceptos himenaeos."</p>
    <div class="name">- Marcus Hale</div>
  </div>
  <div class="quote" style="left:494px">
    <div class="avatar" role="img" aria-label="Customer portrait"></div>
    <div class="qmark">&ldquo;</div>
    <p>"Duis sed odio sit amet nibh vulputate as non mauris vitae erat consequat auctor eu in elit. Class aptent taciti sociosqu ad litora torquent per conubia nostra, per inceptos himenaeos."</p>
    <div class="name">-Lena Ortiz</div>
  </div>
  <div class="quote" style="left:730px">
    <div class="avatar" role="img" aria-label="Customer portrait"></div>
    <div class="qmark">&ldquo;</div>
    <p>"Duis sed odio sit amet nibh vulputate as non mauris vitae erat consequat auctor eu in elit. Class aptent taciti sociosqu ad litora torquent per conubia nostra, per inceptos himenaeos."</p>
    <div class="name">- Rafiq Amin</div>
  </div>
</section>

<section class="abs blog">
  <h2>From The Blog</h2>
  <div class="rule"></div>
  <article class="post" style="left:243px">
    <div class="ph" role="img" aria-label="Solar panels and wind turbines at dusk" style="background:linear-gradient(180deg,#2f5f9c,#7da6cf 55%,#3d5774)"></div>
    <h4>Awesome Lorem ipsum dolor sit amet dosis lipsum it</h4>
    <p>Class aptent taciti sociosqu ad litora torquent per conubia nostra, per himenaeos. Mauris in erat justo.</p>
    <a>Read More &rarr;</a>
  </article>
  <article class="post" style="left:455px">
    <div class="ph" role="img" aria-label="Wind turbines on green hills at sunset" style="background:linear-gradient(180deg,#5d7fb0,#e8c9a0 55%,#5b8a3c)"></div>
    <h4>Awesome Lorem ipsum dolor sit amet dosis lipsum it</h4>
    <p>Class aptent taciti sociosqu ad litora torquent per conubia nostra, per himenaeos. Mauris in erat justo.</p>
    <a>Read More &rarr;</a>
  </article>

  <aside class="why">
    <h3>Why Choose Us</h3>
    <div class="why-item">
      <div class="ic"><svg width="16" height="16" viewBox="0 0 24 24"><text x="12" y="18" text-anchor="middle" font-size="18" font-weight="700" fill="#222" font-family="Roboto,sans-serif">$</text></svg></div>
      <div><h5>Best Price</h5><p>Proin condimentum fermentum mentum feugiat, velit mauris massa nisl quis neque.</p></div>
    </div>
    <div class="why-item">
      <div class="ic"><svg width="16" height="16" viewBox="0 0 24 24"><circle cx="12" cy="9" r="6" fill="none" stroke="#222" stroke-width="2"/><path d="M8 14l-2 8 6-3 6 3-2-8" fill="none" stroke="#222" stroke-width="2"/></svg></div>
      <div><h5>Best Services</h5><p>Proin condimentum fermentum mentum feugiat, velit mauris massa nisl quis neque.</p></div>
    </div>
    <div class="why-item">
      <div class="ic"><svg width="16" height="16" viewBox="0 0 24 24"><path d="M5 12l5 5 9-10" fill="none" stroke="#222" stroke-width="3"/></svg></div>
      <div><h5>Guaranteed</h5><p>Proin condimentum fermentum mentum feugiat, velit mauris massa nisl quis neque.</p></div>
    </div>
  </aside>
</section>

<footer class="abs footer">
  <div class="news">
    <div class="title"><svg width="38" height="22" viewBox="0 0 38 22"><path d="M2 11L36 2 28 20 18 14z" fill="none" stroke="#ccc" stroke-width="2"/><path d="M0 16h10M4 20h8" stroke="#ccc" stroke-width="2"/></svg>SUBSCRIBE<br>OUR NEWSLETTER</div>
    <div class="field">Enter Your Email</div>
    <span class="btn btn-yellow">Subscribe</span>
  </div>
  <div class="fdiv"></div>
  <div class="social"><i></i><i></i><i></i><i></i><i></i></div>

  <div class="fcol" style="left:243px"><h6>Navigation Links</h6>Home<br>About<br>Services<br>Products<br>Testimonials<br>Blog<br>Contact</div>
  <div class="fcol" style="left:426px"><h6>Customer Service</h6>About Us<br>Delivery Information<br>Privacy Policy<br>Terms &amp; Conditions<br>Contact Us<br>Returns<br>Site Map</div>
  <div class="fcol" style="left:607px"><h6>My Account</h6>Order History<br>Wish List<br>Newsletter<br>Gift Vouchers<br>Affiliates<br>Specials</div>
  <div class="fcol" style="left:791px"><h6>Our Location</h6>228, lorem ipsum dolor amet,<br>dosis alt sit - 48596<br><br>T: 1800 555 0199<br>F: 1800 555 0188<br>E: info@brookforge.example<br>www.brookforge.example</div>

  <div class="pay"><i></i><i></i><i></i><i></i></div>
  <div class="copy">&copy; 2018 The Brook Forge. All Rights Reserved</div>
</footer>

</body>
</html>
```